St Louis Electrician Needing a Business Card Design!!

We are a St Louis based electrical contracting firm that needs help designing a business card. We have a logo and I have another image that I would like to incorporate. Open to ideas..Thanks!!

Industry/Entity Type

Business

Requirements
Must have
• there are two downloads...one is the logo and the other is what i was wanting coming off the logo...the light rays. Like the logo with the blue background...Was thinking the whole card would be that color blue.
Should not have
• No lightning bolts

```html
<!DOCTYPE html>
<html lang="en">
<head>
<meta charset="utf-8">
<title>Voltline Electric Inc. — Business Card</title>
<link href="https://fonts.googleapis.com/css2?family=Questrial&display=swap" rel="stylesheet">
<style>
  :root{
    --backdrop:#1a1a1c;
    --card-deep:#142a5e;
    --card-mid:#1b3f86;
    --card-glow:#2456a8;
    --accent:#2aa2ec;
    --streak:#4fb3ff;
    --ink:#ffffff;
  }
  *{margin:0;padding:0;box-sizing:border-box}
  html,body{width:1200px;height:1001px;overflow:hidden;background:var(--backdrop)}
  body{font-family:"Questrial",sans-serif;color:var(--ink);position:relative}
  .card{
    position:absolute;left:306px;width:588px;height:330px;overflow:hidden;
    box-shadow:0 6px 18px rgba(0,0,0,.6);
  }
  .card--front{top:133px;background:radial-gradient(ellipse 70% 90% at 30% 25%,var(--card-glow),var(--card-mid) 45%,var(--card-deep) 100%)}
  .card--back{top:539px;background:radial-gradient(ellipse 60% 80% at 45% 45%,var(--card-glow),var(--card-mid) 45%,var(--card-deep) 100%)}
  .wordmark{position:absolute;font-size:35px;letter-spacing:.5px;line-height:1}
  .wordmark__suffix{display:block;text-align:right;font-size:18px;margin-top:2px}
  .card--front .wordmark{left:46px;top:82px}
  .card--back .wordmark{left:122px;top:148px}
  .streak{position:absolute;height:2px;border-radius:2px;
    background:linear-gradient(90deg,transparent,var(--streak) 30%,rgba(79,179,255,.2) 80%,transparent)}
  .streak--logo{left:0;top:131px;width:260px}
  .streak--logo-thin{left:0;top:142px;width:200px;height:1px;opacity:.6}
  .streak--name{left:300px;top:291px;width:288px;height:1px;
    background:linear-gradient(90deg,transparent,var(--streak) 50%,rgba(79,179,255,.4))}
  .glow{position:absolute;left:200px;top:60px;width:160px;height:160px;border-radius:50%;
    background:radial-gradient(circle,rgba(120,200,255,.45),rgba(80,160,255,.12) 40%,transparent 70%)}
  .address{position:absolute;left:46px;top:188px;font-size:14px;line-height:19px}
  .contacts{position:absolute;left:46px;top:237px;list-style:none;font-size:14px;line-height:19px}
  .contacts li{display:flex;align-items:center;gap:10px}
  .contacts svg{width:15px;height:15px;flex:none}
  .person{position:absolute;right:46px;top:238px;text-align:right}
  .person__name{font-size:17px;color:var(--accent);letter-spacing:.5px;text-transform:uppercase;-webkit-text-stroke:.4px var(--accent)}
  .person__title{font-size:14px;margin-top:3px}
</style>
</head>
<body>
  <section class="card card--front">
    <div class="streak streak--logo"></div>
    <div class="streak streak--logo-thin"></div>
    <div class="wordmark">Voltline Electric<span class="wordmark__suffix">Inc.</span></div>
    <p class="address">418 Harlow Mill Road<br>Fenwick, MO 63021</p>
    <ul class="contacts">
      <li><svg viewBox="0 0 15 15"><rect width="15" height="15" rx="3" fill="#2aa2ec"/><path d="M4.5 3.5l2 .3.6 2-1 .8a6 6 0 0 0 2.4 2.4l.8-1 2 .6.3 2c-4.5.5-7.6-2.6-7.1-7.1z" fill="#fff"/></svg>(314) 555-0172</li>
      <li><svg viewBox="0 0 15 15"><rect width="15" height="15" rx="3" fill="#2aa2ec"/><rect x="3" y="4.5" width="9" height="6" fill="none" stroke="#fff"/><path d="M3 4.5l4.5 3.5 4.5-3.5" fill="none" stroke="#fff"/></svg>info@voltlineelectric.com</li>
      <li><svg viewBox="0 0 15 15"><rect width="15" height="15" rx="3" fill="#2aa2ec"/><circle cx="7.5" cy="7.5" r="4.5" fill="none" stroke="#fff"/><ellipse cx="7.5" cy="7.5" rx="2" ry="4.5" fill="none" stroke="#fff"/><path d="M3 7.5h9" stroke="#fff"/></svg>www.voltlineelectric.com</li>
    </ul>
    <div class="person">
      <div class="person__name">Dana Whitfield</div>
      <div class="person__title">General Manager</div>
    </div>
    <div class="streak streak--name"></div>
  </section>

  <section class="card card--back">
    <div class="glow" role="img" aria-label="Soft burst of blue light near the company name"></div>
    <div class="wordmark">Voltline Electric<span class="wordmark__suffix">Inc.</span></div>
  </section>
</body>
</html>
```